Endocrinologist needs new stationery

I have a logo from MarkForge and now need stationery with the new logo.

Address: Suite 4, 282 Falcon Street, Hawthorn, VIC 3122
Phone: 03 9417 2253
Fax: 03 9417 2255
Website: www.drmaylacorwen.com.au
Email: admin@drmaylacorwen.com.au

```html
<!DOCTYPE html>
<html lang="en">
<head>
<meta charset="utf-8">
<title>Dr Mayla Corwen – Stationery</title>
<link rel="stylesheet" href="https://fonts.googleapis.com/css2?family=Open+Sans:wght@300;400&display=swap">
<style>
  :root {
    --backdrop: #dcd9d4;
    --paper: #f6f6f5;
    --brand-blue: #3e70a1;
    --accent-plum: #8b4a5c;
    --body-text: #6a6a6a;
    --rule: #c9c9c9;
  }
  * { box-sizing: border-box; margin: 0; padding: 0; }
  html, body { width: 1200px; height: 1200px; overflow: hidden; }
  body {
    position: relative;
    background: var(--backdrop);
    font-family: "Open Sans", Arial, sans-serif;
    color: var(--body-text);
  }

  /* Letterhead */
  .letterhead {
    position: absolute;
    width: 478px; height: 677px;
    background: var(--paper);
    overflow: hidden;
  }
  .letterhead--back { left: -102px; top: 145px; }
  .letterhead--front { left: 400px; top: 288px; }

  .brand {
    position: absolute;
    display: flex; align-items: center; gap: 6px;
    color: var(--brand-blue);
    font-weight: 400;
    white-space: nowrap;
  }
  .brand__dot { width: 7px; height: 7px; border-radius: 50%; background: var(--brand-blue); }
  .letterhead .brand { right: 24px; top: 26px; font-size: 17px; letter-spacing: .5px; }

  .letterhead__divider {
    position: absolute; left: 349px; top: 72px;
    width: 1px; height: 530px; background: var(--rule);
  }
  .contact {
    position: absolute; left: 361px;
    font-size: 6.6px; line-height: 11.5px; color: var(--body-text);
    white-space: nowrap;
  }
  .contact li { list-style: none; display: flex; align-items: flex-start; gap: 4px; }
  .contact svg { flex: none; width: 6px; height: 6px; margin-top: 2.5px; }
  .contact--top { top: 84px; }
  .contact--bottom { top: 581px; }
  .contact .gap { height: 8px; }

  .letter {
    position: absolute; left: 28px; top: 76px; width: 299px;
    font-size: 8px; line-height: 13.3px; font-weight: 400;
    letter-spacing: .3px; color: var(--body-text);
  }
  .letter__date, .letter__recipient { margin-bottom: 13px; }
  .letter p.body { text-align: justify; hyphens: auto; margin-bottom: 13.3px; }
  .signature {
    width: 138px; height: 30px; margin-top: 6px;
    background: linear-gradient(90deg, rgba(139,74,92,.18), rgba(139,74,92,.06));
    border-radius: 4px;
  }

  .letterhead__band {
    position: absolute; left: 205px; right: 0; bottom: 0; height: 22px;
    background: var(--brand-blue);
  }
  .letterhead__mark {
    position: absolute; left: 205px; bottom: 4px;
    width: 18px; height: 18px; border-radius: 50%;
    background: var(--paper); border: 1.5px solid var(--brand-blue);
  }

  /* Business cards */
  .card { position: absolute; width: 195px; height: 124px; overflow: hidden; }
  .card--front { left: 898px; top: 288px; background: var(--paper); }
  .card--back { left: 900px; top: 432px; background: var(--brand-blue); }
  .card--front .brand { right: 14px; top: 18px; font-size: 10px; }
  .card__rule { position: absolute; left: 76px; right: 14px; top: 39px; height: 1px; background: var(--rule); }
  .card .contact { left: 76px; top: 52px; font-size: 5px; line-height: 7.6px; }
  .card .contact svg { width: 4px; height: 4px; margin-top: 1.8px; }
  .card .contact .gap { height: 6px; }
  .card__band { position: absolute; left: 88px; right: 0; bottom: 0; height: 9px; background: var(--brand-blue); }
  .card__mark { position: absolute; left: 86px; bottom: 1px; width: 10px; height: 10px; border-radius: 50%; background: var(--paper); border: 1px solid var(--brand-blue); }
  .card--back .brand { right: 14px; top: 80px; font-size: 12px; color: #fff; }
  .card--back .brand__dot { background: #fff; }
  .card--back .card__rule { left: 64px; top: 105px; background: rgba(255,255,255,.6); }
  .card--back .card__strip { position: absolute; left: 40px; right: 0; bottom: 0; height: 8px; background: var(--paper); }
  .card--back .card__mark { left: 38px; bottom: 0; background: var(--brand-blue); border-color: var(--paper); }

  /* Envelope */
  .envelope { position: absolute; left: 905px; top: 580px; width: 225px; height: 478px; background: var(--paper); overflow: hidden; }
  .envelope__strip {
    position: absolute; right: 0; top: 0; width: 23px; height: 230px;
    background: var(--brand-blue);
    display: flex; align-items: center; justify-content: center;
  }
  .envelope__address {
    writing-mode: vertical-rl; transform: rotate(180deg);
    color: #fff; font-size: 8.2px; white-space: nowrap;
  }
  .envelope__mark {
    position: absolute; right: 12px; top: 224px;
    width: 14px; height: 14px; border-radius: 50%;
    background: var(--paper); border: 1.5px solid var(--brand-blue);
  }
  .envelope .brand {
    left: 28px; bottom: 28px;
    writing-mode: vertical-rl; transform: rotate(180deg);
    font-size: 17px; letter-spacing: .5px;
  }
  .envelope__rule { position: absolute; left: 56px; bottom: 78px; width: 1px; height: 108px; background: var(--rule); }
</style>
</head>
<body>

<!-- Letterhead, rear sheet -->
<section class="letterhead letterhead--back">
  <div class="brand"><span class="brand__dot"></span>Dr Mayla Corwen</div>
  <div class="letterhead__divider"></div>
  <ul class="contact contact--top">
    <li><svg viewBox="0 0 6 6"><rect x="1" y="0.5" width="4" height="5" rx="1" fill="var(--accent-plum)"/></svg>03 9417 2253</li>
    <li><svg viewBox="0 0 6 6"><rect x="0" y="1" width="6" height="4" fill="var(--accent-plum)"/></svg>admin@drmaylacorwen.com.au</li>
  </ul>
  <div class="letter" lang="en">
    <p class="letter__date">&nbsp;</p>
    <p class="letter__recipient">To the Former Company name.:</p>
    <p class="body">Lorem Ipsum is simply dummy text of the printing and typesetting industry. Lorem Ipsum has been the industry's standard dummy text ever since the 1500s, when an unknown printer took a galley of type and scrambled it to make a type specimen book. It has survived not only five centuries, but also the leap into electronic typesetting, remaining essentially unchanged. It was popularised in the 1960s with the release of Printwell sheets containing Lorem Ipsum passages, and more recently with desktop publishing software like Folio Layout including versions of Lorem Ipsum.Lorem Ipsum is simply dummy text of the printing and typesetting industry.</p>
    <p class="body">Lorem Ipsum has been the industry's standard dummy text ever since the 1500s, when an unknown printer took a galley of type and scrambled it to make a type specimen book. It has survived not only five centuries, but also the leap into electronic typesetting, remaining essentially unchanged. It was popularised in the 1960s with the release of Printwell sheets containing Lorem Ipsum passages, and more recently with desktop publishing software like Folio Layout including versions of Lorem Ipsum.</p>
    <p class="body">Lorem Ipsum is simply dummy text of the printing and typesetting industry. Lorem Ipsum has been the industry's standard dummy text ever since the 1500s, when an unknown printer took a galley of type and scrambled it to make a type specimen book. It has survived not only five centuries, but also the leap into electronic typesetting, remaining essentially unchanged. It was popularised in the 1960s with the release of Printwell sheets containing Lorem Ipsum passages, and more recently with desktop publishing software like Folio Layout including versions of Lorem Ipsum.</p>
    <p class="letter__closing">Sincerely yours,</p>
    <div class="signature" role="img" aria-label="Handwritten signature of Dr Mayla Corwen"></div>
  </div>
  <ul class="contact contact--bottom">
    <li><svg viewBox="0 0 6 6"><path d="M3 6 L0.8 2.8 A2.3 2.3 0 1 1 5.2 2.8 Z" fill="var(--accent-plum)"/></svg>Suite 4, 282 Falcon Street,<br>Hawthorn, VIC 3122</li>
    <li class="gap"></li>
    <li><svg viewBox="0 0 6 6"><rect x="0.5" y="1" width="5" height="4" rx="1" fill="var(--accent-plum)"/></svg>03 9417 2255</li>
    <li><svg viewBox="0 0 6 6"><circle cx="3" cy="3" r="2.5" fill="none" stroke="var(--accent-plum)"/></svg>www.drmaylacorwen.com.au</li>
  </ul>
  <div class="letterhead__band"></div>
  <div class="letterhead__mark"></div>
</section>

<!-- Letterhead, front sheet -->
<section class="letterhead letterhead--front">
  <div class="brand"><span class="brand__dot"></span>Dr Mayla Corwen</div>
  <div class="letterhead__divider"></div>
  <ul class="contact contact--top">
    <li><svg viewBox="0 0 6 6"><rect x="1" y="0.5" width="4" height="5" rx="1" fill="var(--accent-plum)"/></svg>03 9417 2253</li>
    <li><svg viewBox="0 0 6 6"><rect x="0" y="1" width="6" height="4" fill="var(--accent-plum)"/></svg>admin@drmaylacorwen.com.au</li>
  </ul>
  <div class="letter" lang="en">
    <p class="letter__date">MAY 05,2026</p>
    <p class="letter__recipient">To the Former Company name.:</p>
    <p class="body">Lorem Ipsum is simply dummy text of the printing and typesetting industry. Lorem Ipsum has been the industry's standard dummy text ever since the 1500s, when an unknown printer took a galley of type and scrambled it to make a type specimen book. It has survived not only five centuries, but also the leap into electronic typesetting, remaining essentially unchanged. It was popularised in the 1960s with the release of Printwell sheets containing Lorem Ipsum passages, and more recently with desktop publishing software like Folio Layout including versions of Lorem Ipsum.Lorem Ipsum is simply dummy text of the printing and typesetting industry.</p>
    <p class="body">Lorem Ipsum has been the industry's standard dummy text ever since the 1500s, when an unknown printer took a galley of type and scrambled it to make a type specimen book. It has survived not only five centuries, but also the leap into electronic typesetting, remaining essentially unchanged. It was popularised in the 1960s with the release of Printwell sheets containing Lorem Ipsum passages, and more recently with desktop publishing software like Folio Layout including versions of Lorem Ipsum.</p>
    <p class="body">Lorem Ipsum is simply dummy text of the printing and typesetting industry. Lorem Ipsum has been the industry's standard dummy text ever since the 1500s, when an unknown printer took a galley of type and scrambled it to make a type specimen book. It has survived not only five centuries, but also the leap into electronic typesetting, remaining essentially unchanged. It was popularised in the 1960s with the release of Printwell sheets containing Lorem Ipsum passages, and more recently with desktop publishing software like Folio Layout including versions of Lorem Ipsum.</p>
    <p class="letter__closing">Sincerely yours,</p>
    <div class="signature" role="img" aria-label="Handwritten signature of Dr Mayla Corwen"></div>
  </div>
  <ul class="contact contact--bottom">
    <li><svg viewBox="0 0 6 6"><path d="M3 6 L0.8 2.8 A2.3 2.3 0 1 1 5.2 2.8 Z" fill="var(--accent-plum)"/></svg>Suite 4, 282 Falcon Street,<br>Hawthorn, VIC 3122</li>
    <li class="gap"></li>
    <li><svg viewBox="0 0 6 6"><rect x="0.5" y="1" width="5" height="4" rx="1" fill="var(--accent-plum)"/></svg>03 9417 2255</li>
    <li><svg viewBox="0 0 6 6"><circle cx="3" cy="3" r="2.5" fill="none" stroke="var(--accent-plum)"/></svg>www.drmaylacorwen.com.au</li>
  </ul>
  <div class="letterhead__band"></div>
  <div class="letterhead__mark"></div>
</section>

<!-- Business card, front -->
<section class="card card--front">
  <div class="brand"><span class="brand__dot"></span>Dr Mayla Corwen</div>
  <div class="card__rule"></div>
  <ul class="contact">
    <li><svg viewBox="0 0 6 6"><path d="M3 6 L0.8 2.8 A2.3 2.3 0 1 1 5.2 2.8 Z" fill="var(--accent-plum)"/></svg>Suite 4, 282 Falcon Street,<br>Hawthorn, VIC 3122</li>
    <li class="gap"></li>
    <li><svg viewBox="0 0 6 6"><rect x="1" y="0.5" width="4" height="5" rx="1" fill="var(--accent-plum)"/></svg>03 9417 2253</li>
    <li><svg viewBox="0 0 6 6"><rect x="0.5" y="1" width="5" height="4" rx="1" fill="var(--accent-plum)"/></svg>03 9417 2255</li>
    <li class="gap"></li>
    <li><svg viewBox="0 0 6 6"><circle cx="3" cy="3" r="2.5" fill="none" stroke="var(--accent-plum)"/></svg>www.drmaylacorwen.com.au</li>
    <li><svg viewBox="0 0 6 6"><rect x="0" y="1" width="6" height="4" fill="var(--accent-plum)"/></svg>admin@drmaylacorwen.com.au</li>
  </ul>
  <div class="card__band"></div>
  <div class="card__mark"></div>
</section>

<!-- Business card, back -->
<section class="card card--back">
  <div class="brand"><span class="brand__dot"></span>Dr Mayla Corwen</div>
  <div class="card__rule"></div>
  <div class="card__strip"></div>
  <div class="card__mark"></div>
</section>

<!-- Envelope -->
<section class="envelope">
  <div class="envelope__strip">
    <span class="envelope__address">Suite 4, 282 Falcon Street, Hawthorn, VIC 3122</span>
  </div>
  <div class="envelope__mark"></div>
  <div class="envelope__rule"></div>
  <div class="brand"><span class="brand__dot"></span>Dr Mayla Corwen</div>
</section>

</body>
</html>
```